Educational outcome management software startup firm needs a graphic design

Our software startup firm, Kravix Metric Systems recently purchased a beautiful logo from Plumwerk (uploaded file). We are now looking for a graphic design to be used in the marketing activities of Kravix Metric Systems. See the uploaded picture of what a sketch of the graphic we are looking for.

```html
<!DOCTYPE html>
<html lang="en">
<head>
<meta charset="utf-8">
<title>Learner Wheel of Success – Kravix Metric Systems</title>
<link href="https://fonts.googleapis.com/css2?family=Montserrat:wght@500;700&display=swap" rel="stylesheet">
<style>
  :root {
    --page: #eef0f3;
    --navy-deep: #0b0d33;
    --navy: #161b5a;
    --navy-glow: #2a3594;
    --orange: #d9512c;
    --orange-soft: #f07a4f;
    --white: #ffffff;
    --ring: rgba(255,255,255,0.55);
    --brand: #1d2a6b;
  }
  html, body {
    margin: 0;
    width: 1200px;
    height: 3398px;
    overflow: hidden;
    background: var(--page);
    font-family: "Montserrat", Arial, sans-serif;
  }
  .poster {
    position: absolute;
    left: 50px;
    top: 988px;
    width: 1100px;
    height: 1422px;
    box-shadow: 0 18px 40px rgba(0,0,0,0.18);
  }
  .poster svg { display: block; width: 100%; height: 100%; }
  .title-top { fill: var(--orange); font-weight: 500; font-size: 54px; letter-spacing: 1px; }
  .title-main { fill: var(--white); font-weight: 500; font-size: 120px; letter-spacing: 2px; }
  .label { fill: var(--white); font-weight: 700; font-size: 12px; }
  .center-label { fill: var(--white); font-weight: 700; font-size: 17px; }
  .brand-name { fill: var(--brand); font-weight: 700; font-size: 26px; }
  .ring { fill: none; stroke: var(--ring); stroke-width: 1; stroke-dasharray: 1.5 2.5; }
  .ring-inner { fill: none; stroke: rgba(255,255,255,0.35); stroke-width: 1; }
  .waypoint { fill: var(--orange); stroke: rgba(255,255,255,0.6); stroke-width: 1; }
  .node-orange { fill: var(--orange); stroke: var(--white); stroke-width: 3; }
  .node-white { fill: var(--white); stroke: rgba(255,255,255,0.5); stroke-width: 3; }
  .icon-light { fill: var(--white); stroke: none; }
  .icon-light-line { fill: none; stroke: var(--white); stroke-width: 2; }
  .icon-dark { fill: var(--brand); stroke: none; }
  .icon-dark-line { fill: none; stroke: var(--brand); stroke-width: 2; }
  .star { fill: rgba(255,255,255,0.7); }
  .footer-band { fill: var(--white); }
</style>
</head>
<body>
<div class="poster">
<svg viewBox="0 0 800 1034" xmlns="http://www.w3.org/2000/svg" role="img" aria-label="Learner Wheel of Success poster">
  <defs>
    <radialGradient id="space" cx="50%" cy="52%" r="60%">
      <stop offset="0" stop-color="var(--navy-glow)"/>
      <stop offset="0.45" stop-color="var(--navy)"/>
      <stop offset="1" stop-color="var(--navy-deep)"/>
    </radialGradient>
    <radialGradient id="core-glow" cx="50%" cy="50%" r="50%">
      <stop offset="0" stop-color="var(--orange-soft)" stop-opacity="0.9"/>
      <stop offset="0.55" stop-color="var(--orange)" stop-opacity="0.35"/>
      <stop offset="1" stop-color="var(--orange)" stop-opacity="0"/>
    </radialGradient>
    <radialGradient id="node-glow" cx="50%" cy="50%" r="50%">
      <stop offset="0.5" stop-color="var(--orange)" stop-opacity="0.55"/>
      <stop offset="1" stop-color="var(--orange)" stop-opacity="0"/>
    </radialGradient>
    <radialGradient id="white-glow" cx="50%" cy="50%" r="50%">
      <stop offset="0.5" stop-color="#ffffff" stop-opacity="0.35"/>
      <stop offset="1" stop-color="#ffffff" stop-opacity="0"/>
    </radialGradient>
    <linearGradient id="band-fade" x1="0" y1="0" x2="0" y2="1">
      <stop offset="0" stop-color="#ffffff" stop-opacity="0"/>
      <stop offset="0.5" stop-color="#ffffff" stop-opacity="0.9"/>
      <stop offset="1" stop-color="#ffffff"/>
    </linearGradient>
  </defs>

  <!-- backdrop -->
  <rect class="backdrop" width="800" height="1034" fill="url(#space)"/>
  <g class="stars">
    <circle class="star" cx="40" cy="60" r="1"/><circle class="star" cx="120" cy="120" r="0.8"/>
    <circle class="star" cx="760" cy="40" r="1"/><circle class="star" cx="700" cy="190" r="0.8"/>
    <circle class="star" cx="60" cy="300" r="1.1"/><circle class="star" cx="30" cy="480" r="0.8"/>
    <circle class="star" cx="770" cy="420" r="1"/><circle class="star" cx="740" cy="700" r="0.9"/>
    <circle class="star" cx="50" cy="820" r="1"/><circle class="star" cx="200" cy="880" r="0.8"/>
    <circle class="star" cx="620" cy="880" r="1"/><circle class="star" cx="780" cy="860" r="0.8"/>
    <circle class="star" cx="260" cy="220" r="0.8"/><circle class="star" cx="560" cy="230" r="0.9"/>
    <circle class="star" cx="150" cy="650" r="0.8"/><circle class="star" cx="680" cy="520" r="0.8"/>
    <circle class="star" cx="330" cy="30" r="0.8"/><circle class="star" cx="480" cy="180" r="0.7"/>
  </g>

  <!-- title -->
  <text class="title-top" x="400" y="68" text-anchor="middle">LEARNER WHEEL OF</text>
  <text class="title-main" x="400" y="157" text-anchor="middle">SUCCESS</text>

  <!-- rings -->
  <circle class="ring" cx="406" cy="542" r="298"/>
  <circle class="ring" cx="406" cy="542" r="218"/>
  <circle class="ring-inner" cx="406" cy="542" r="162"/>

  <!-- core -->
  <circle cx="406" cy="545" r="120" fill="url(#core-glow)"/>
  <circle cx="406" cy="545" r="72" fill="var(--orange)" stroke="var(--white)" stroke-width="4"/>
  <g class="icon-cap" transform="translate(406 518)">
    <path class="icon-light" d="M-24 -4 L0 -14 L24 -4 L0 6 Z"/>
    <path class="icon-light" d="M-14 2 L0 8 L14 2 V12 C8 17 -8 17 -14 12 Z"/>
    <path class="icon-light-line" d="M20 -3 V12"/>
    <circle class="icon-light" cx="20" cy="14" r="2.5"/>
  </g>
  <text class="center-label" x="406" y="570" text-anchor="middle">LEARNER/</text>
  <text class="center-label" x="406" y="588" text-anchor="middle">STUDENT</text>

  <!-- inner skills -->
  <g class="labels-inner">
    <text class="label" x="407" y="406" text-anchor="middle">READING</text>
    <text class="label" x="407" y="420" text-anchor="middle">SKILLS</text>
    <text class="label" x="289" y="467" text-anchor="middle">STEM</text>
    <text class="label" x="289" y="481" text-anchor="middle">SKILLS</text>
    <text class="label" x="520" y="467" text-anchor="middle">WRITING</text>
    <text class="label" x="520" y="481" text-anchor="middle">SKILLS</text>
    <text class="label" x="290" y="600" text-anchor="middle">SOCIAL</text>
    <text class="label" x="290" y="614" text-anchor="middle">SKILLS</text>
    <text class="label" x="524" y="600" text-anchor="middle">STUDY</text>
    <text class="label" x="524" y="614" text-anchor="middle">SKILLS</text>
    <text class="label" x="407" y="668" text-anchor="middle">INFORMATION</text>
    <text class="label" x="407" y="682" text-anchor="middle">TECHNOLOGY</text>
    <text class="label" x="407" y="696" text-anchor="middle">SKILLS</text>
  </g>

  <!-- milestones on middle ring -->
  <g class="waypoints">
    <circle class="waypoint" cx="346" cy="330" r="3.5"/><circle class="waypoint" cx="458" cy="326" r="3.5"/>
    <circle class="waypoint" cx="256" cy="383" r="3.5"/><circle class="waypoint" cx="231" cy="418" r="3.5"/>
    <circle class="waypoint" cx="558" cy="383" r="3.5"/><circle class="waypoint" cx="588" cy="418" r="3.5"/>
    <circle class="waypoint" cx="191" cy="532" r="3.5"/><circle class="waypoint" cx="198" cy="603" r="3.5"/>
    <circle class="waypoint" cx="625" cy="532" r="3.5"/><circle class="waypoint" cx="617" cy="603" r="3.5"/>
    <circle class="waypoint" cx="337" cy="764" r="3.5"/><circle class="waypoint" cx="460" cy="760" r="3.5"/>
  </g>
  <g class="labels-milestones">
    <text class="label" x="400" y="321" text-anchor="middle">HIGH SCHOOL</text>
    <text class="label" x="400" y="335" text-anchor="middle">GRADUATION</text>
    <text class="label" x="243" y="404" text-anchor="middle">ENTREPRENEUR</text>
    <text class="label" x="578" y="404" text-anchor="middle">EMPLOYMENT</text>
    <text class="label" x="191" y="550" text-anchor="middle">GRADUATION</text>
    <text class="label" x="191" y="564" text-anchor="middle">FROM</text>
    <text class="label" x="191" y="578" text-anchor="middle">HIGHER</text>
    <text class="label" x="191" y="592" text-anchor="middle">EDUCATION</text>
    <text class="label" x="623" y="550" text-anchor="middle">ADMISSION</text>
    <text class="label" x="623" y="564" text-anchor="middle">INTO</text>
    <text class="label" x="623" y="578" text-anchor="middle">POST-SECONDARY</text>
    <text class="label" x="623" y="592" text-anchor="middle">INSTITUTION</text>
    <text class="label" x="400" y="762" text-anchor="middle">COMPLETION</text>
    <text class="label" x="400" y="776" text-anchor="middle">OF ELEMENTARY</text>
    <text class="label" x="400" y="790" text-anchor="middle">SCHOOL</text>
  </g>

  <!-- stakeholder nodes -->
  <g class="nodes">
    <!-- parent / guardian: heart -->
    <circle cx="406" cy="242" r="44" fill="url(#node-glow)"/>
    <circle class="node-orange" cx="406" cy="242" r="28"/>
    <g transform="translate(406 242)">
      <path class="icon-light" d="M0 13 C-8 7 -14 2 -14 -4 C-14 -9 -10 -12 -6 -12 C-3 -12 -1 -10 0 -8 C1 -10 3 -12 6 -12 C10 -12 14 -9 14 -4 C14 2 8 7 0 13 Z"/>
    </g>

    <!-- teacher: board with pointer -->
    <circle cx="179" cy="345" r="40" fill="url(#white-glow)"/>
    <circle class="node-white" cx="179" cy="345" r="28"/>
    <g transform="translate(179 345)">
      <rect class="icon-dark-line" x="-10" y="-12" width="22" height="15"/>
      <path class="icon-dark-line" d="M-4 -6 L3 -2 L8 -8"/>
      <path class="icon-dark-line" d="M-14 14 L-4 3"/>
      <path class="icon-dark-line" d="M1 3 V14 M-6 14 H8"/>
    </g>

    <!-- employer: briefcase -->
    <circle cx="637" cy="350" r="40" fill="url(#white-glow)"/>
    <circle class="node-white" cx="637" cy="350" r="28"/>
    <g transform="translate(637 350)">
      <rect class="icon-dark-line" x="-5" y="-12" width="10" height="6" rx="1"/>
      <rect class="icon-dark" x="-13" y="-7" width="26" height="18" rx="2"/>
      <rect x="-3" y="0" width="6" height="4" fill="var(--white)"/>
    </g>

    <!-- school counselor: school building -->
    <circle cx="100" cy="545" r="44" fill="url(#node-glow)"/>
    <circle class="node-orange" cx="100" cy="545" r="28"/>
    <g transform="translate(100 545)">
      <path class="icon-light" d="M-14 -2 L0 -12 L14 -2 Z"/>
      <rect class="icon-light" x="-13" y="-1" width="26" height="14"/>
      <g fill="var(--orange)">
        <rect x="-10" y="2" width="4" height="4"/><rect x="-2" y="2" width="4" height="4"/><rect x="6" y="2" width="4" height="4"/>
        <rect x="-2" y="8" width="4" height="5"/>
      </g>
    </g>

    <!-- post-secondary: monitor -->
    <circle cx="712" cy="545" r="44" fill="url(#node-glow)"/>
    <circle class="node-orange" cx="712" cy="545" r="28"/>
    <g transform="translate(712 545)">
      <rect class="icon-light-line" x="-13" y="-11" width="26" height="17" rx="1.5"/>
      <path class="icon-light" d="M-7 -5 L0 -8 L7 -5 L0 -2 Z"/>
      <rect class="icon-light" x="-6" y="0" width="12" height="2"/>
      <path class="icon-light-line" d="M0 6 V11 M-6 12 H6"/>
    </g>

    <!-- school administrator: desk with speech bubble -->
    <circle cx="172" cy="740" r="40" fill="url(#white-glow)"/>
    <circle class="node-white" cx="172" cy="740" r="28"/>
    <g transform="translate(172 740)">
      <rect class="icon-dark" x="-2" y="-14" width="14" height="9" rx="2"/>
      <path class="icon-dark" d="M2 -5 L0 -1 L6 -5 Z"/>
      <rect class="icon-dark" x="-14" y="2" width="28" height="3"/>
      <path class="icon-dark-line" d="M-11 5 V13 M11 5 V13"/>
      <rect class="icon-dark" x="-8" y="-4" width="9" height="6"/>
    </g>

    <!-- government: columned building -->
    <circle cx="634" cy="740" r="40" fill="url(#white-glow)"/>
    <circle class="node-white" cx="634" cy="740" r="28"/>
    <path class="icon-dark" d="M621 736 L634 728 L647 736 Z M623 738 h3 v10 h-3 Z M632.5 738 h3 v10 h-3 Z M642 738 h3 v10 h-3 Z M620 749 h28 v3 h-28 Z"/>

    <!-- international marketplace: storefront -->
    <circle cx="406" cy="837" r="44" fill="url(#node-glow)"/>
    <circle class="node-orange" cx="406" cy="837" r="28"/>
    <g transform="translate(406 837)">
      <path class="icon-light" d="M-14 -12 H14 L15 -4 H-15 Z"/>
      <rect class="icon-light" x="-12" y="-3" width="24" height="16"/>
      <rect x="-8" y="1" width="6" height="12" fill="var(--orange)"/>
      <rect x="2" y="1" width="7" height="6" fill="var(--orange)"/>
    </g>
  </g>
  <g class="labels-nodes">
    <text class="label" x="406" y="196" text-anchor="middle">PARENT/GUARDIAN</text>
    <text class="label" x="100" y="340" text-anchor="middle">TEACHER</text>
    <text class="label" x="714" y="340" text-anchor="middle">EMPLOYER</text>
    <text class="label" x="103" y="598" text-anchor="middle">SCHOOL</text>
    <text class="label" x="103" y="612" text-anchor="middle">COUNSELOR</text>
    <text class="label" x="710" y="609" text-anchor="middle">POST-</text>
    <text class="label" x="710" y="623" text-anchor="middle">SECONDARY</text>
    <text class="label" x="710" y="637" text-anchor="middle">EDUCATION</text>
    <text class="label" x="710" y="651" text-anchor="middle">SYSTEMS</text>
    <text class="label" x="115" y="793" text-anchor="middle">SCHOOL</text>
    <text class="label" x="115" y="807" text-anchor="middle">ADMINISTRATOR</text>
    <text class="label" x="662" y="793" text-anchor="middle">GOVERNMENT</text>
    <text class="label" x="408" y="890" text-anchor="middle">INTERNATION</text>
    <text class="label" x="408" y="904" text-anchor="middle">MARKET PLACE</text>
  </g>

  <!-- footer band -->
  <rect x="0" y="925" width="800" height="30" fill="url(#band-fade)" role="img" aria-label="Soft cloud border"/>
  <rect class="footer-band" x="0" y="954" width="800" height="80"/>

  <!-- brand -->
  <g class="brand">
    <circle cx="262" cy="995" r="7" fill="var(--orange)"/>
    <text class="brand-name" x="278" y="1004">Kravix Metric Systems</text>
  </g>
</svg>
</div>
</body>
</html>
```